Harwick Construction LTD is in need of a web page we are renovation and maintenance specialists

We are a medium size building company specialising in renovations and maintainance on commercial and residential properties bathrooms, kitchens, alterations, commercial shop fit outs, office fit outs. we also specialise in project management taking care of all manners of trades from concept to completion with trade qualified LBP registered builders customers can be assured that they will get the best possible results

Industry/Entity Type

Building

Coding

Coded - Design and coding required

Number of Pages Required

2 page

```html
<!DOCTYPE html>
<html lang="en">
<head>
<meta charset="utf-8">
<title>Harwick Construction LTD</title>
<link href="https://fonts.googleapis.com/css2?family=Open+Sans:wght@400;600;700;800&display=swap" rel="stylesheet">
<style>
  :root {
    --navy: #23417f;
    --navy-dark: #1a315f;
    --navy-deep: #142649;
    --sky-top: #6f8fb8;
    --sky-bottom: #1d2f52;
    --ink: #333a45;
    --muted: #7a808a;
    --line: #dfe3ea;
    --white: #ffffff;
    --paper: #f4f6f9;
  }
  * { box-sizing: border-box; margin: 0; padding: 0; }
  html, body { width: 778px; height: 1200px; overflow: hidden; }
  body {
    font-family: "Open Sans", Arial, sans-serif;
    color: var(--ink);
    background: var(--white);
  }
  .page { width: 778px; height: 1200px; display: flex; flex-direction: column; overflow: hidden; }

  /* Header */
  .site-header {
    height: 78px; flex: none; padding: 0 34px;
    display: flex; align-items: center; justify-content: space-between;
    background: var(--white);
  }
  .brand { display: flex; align-items: center; gap: 10px; }
  .brand-mark { width: 16px; height: 16px; background: var(--navy); }
  .brand-name {
    font-weight: 800; font-size: 19px; color: var(--navy);
    letter-spacing: 0.3px; text-transform: uppercase; line-height: 1;
  }
  .main-nav { display: flex; gap: 4px; }
  .main-nav a {
    font-size: 9.5px; font-weight: 600; text-transform: uppercase;
    color: var(--ink); text-decoration: none; padding: 8px 10px; letter-spacing: 0.4px;
  }
  .main-nav a.is-active { background: var(--navy); color: var(--white); }

  /* Hero */
  .hero {
    position: relative; height: 280px; flex: none;
    background: linear-gradient(180deg, var(--sky-top) 0%, #3f5f8f 45%, var(--sky-bottom) 100%);
  }
  .hero-caption { position: absolute; left: 180px; top: 64px; display: flex; flex-direction: column; align-items: flex-start; gap: 8px; }
  .hero-title {
    font-size: 30px; font-weight: 600; color: var(--white);
    background: rgba(20, 38, 73, 0.72); padding: 6px 16px;
  }
  .hero-tag {
    font-size: 18px; color: var(--white);
    background: rgba(35, 65, 127, 0.8); padding: 5px 14px;
  }
  .hero-dots { position: absolute; right: 30px; bottom: 16px; display: flex; gap: 6px; }
  .hero-dots span { width: 8px; height: 8px; border-radius: 50%; background: rgba(255,255,255,0.5); }
  .hero-dots span:first-child { background: var(--white); }

  /* Welcome */
  .welcome { flex: none; padding: 28px 60px 24px; text-align: center; }
  .section-title {
    font-size: 15px; font-weight: 700; text-transform: uppercase;
    color: var(--navy); letter-spacing: 0.4px;
  }
  .welcome-text { margin: 12px auto 0; font-size: 10.5px; line-height: 1.7; color: var(--muted); max-width: 640px; }
  .services { display: flex; justify-content: space-between; margin-top: 24px; padding: 0 30px; }
  .service { width: 170px; display: flex; flex-direction: column; align-items: center; }
  .service-icon {
    width: 82px; height: 82px; border-radius: 50%; background: var(--navy);
    display: flex; align-items: center; justify-content: center;
  }
  .service-name { margin-top: 12px; font-size: 12.5px; font-weight: 700; color: var(--navy); }
  .service-text { margin-top: 6px; font-size: 9.5px; line-height: 1.6; color: var(--muted); }

  /* Latest project band */
  .project-band {
    height: 140px; flex: none; background: linear-gradient(180deg, #2d4c8a, var(--navy-dark));
    color: var(--white); text-align: center; padding: 22px 90px 0;
  }
  .project-band .section-title { color: var(--white); font-size: 13px; }
  .project-text { margin-top: 8px; font-size: 10px; line-height: 1.7; color: #d6deeb; }
  .button {
    display: inline-block; margin-top: 12px; padding: 6px 18px;
    border: 1px solid var(--white); font-size: 9.5px; font-weight: 600;
    color: var(--white); text-transform: uppercase; letter-spacing: 0.5px;
  }

  /* Team */
  .team { height: 200px; flex: none; background: var(--paper); padding: 20px 40px 0; text-align: center; }
  .team-row { display: flex; align-items: center; justify-content: center; gap: 18px; margin-top: 14px; }
  .arrow-btn {
    width: 28px; height: 28px; border-radius: 50%; background: var(--white);
    border: 1px solid var(--line); display: flex; align-items: center; justify-content: center;
  }
  .member { width: 112px; }
  .member-photo { height: 86px; background: linear-gradient(180deg, #c9ced6, #565e6c); }
  .member-name { margin-top: 6px; font-size: 10px; font-weight: 700; color: var(--navy); }
  .member-role { font-size: 8.5px; color: var(--muted); }

  /* Footer */
  .site-footer { flex: 1; background: var(--navy-deep); color: #c4cddd; padding: 20px 40px 0; }
  .footer-cols { display: flex; justify-content: space-between; }
  .footer-col h4 { font-size: 10.5px; color: var(--white); font-weight: 700; margin-bottom: 8px; }
  .footer-col p, .footer-col li { font-size: 9px; line-height: 1.75; list-style: none; }
  .contact-line { display: flex; align-items: center; gap: 6px; }
  .social { display: flex; gap: 6px; }
  .social span { width: 20px; height: 20px; border-radius: 50%; background: var(--navy); }
  .subscribe { display: flex; margin-top: 2px; }
  .subscribe-field { width: 110px; height: 22px; background: var(--white); font-size: 8.5px; color: var(--muted); padding: 5px 6px; }
  .subscribe-btn { height: 22px; background: var(--navy); color: var(--white); font-size: 8.5px; font-weight: 600; padding: 5px 8px; }
  .footer-brand { margin-top: 12px; font-weight: 800; font-size: 12px; color: var(--white); text-transform: uppercase; }
  .copyright { margin-top: 12px; border-top: 1px solid rgba(255,255,255,0.12); padding-top: 8px; font-size: 8.5px; color: #8e9ab0; text-align: center; }
</style>
</head>
<body>
<div class="page">

  <header class="site-header">
    <div class="brand">
      <span class="brand-mark"></span>
      <span class="brand-name">Harwick Construction LTD</span>
    </div>
    <nav class="main-nav">
      <a href="#" class="is-active">Home</a>
      <a href="#">About</a>
      <a href="#">Services</a>
      <a href="#">Projects</a>
      <a href="#">Team</a>
      <a href="#">Contact</a>
    </nav>
  </header>

  <section class="hero" role="img" aria-label="City skyline of office towers at dusk">
    <div class="hero-caption">
      <div class="hero-title">Welcome to Harwick</div>
      <div class="hero-tag">Renovation Specialists</div>
      <div class="hero-tag">Residential and Commercial Fit Outs</div>
    </div>
    <div class="hero-dots"><span></span><span></span><span></span></div>
  </section>

  <section class="welcome">
    <h2 class="section-title">Welcome to Harwick Construction LTD</h2>
    <p class="welcome-text">Harwick Construction LTD is a medium size building company specialising in renovations and maintenance of commercial and residential properties. From bathrooms, kitchens and alterations to shop and office fit outs, our trade qualified LBP registered builders manage every project from concept to completion and deliver the best possible results.</p>

    <div class="services">
      <div class="service">
        <div class="service-icon">
          <svg width="40" height="40" viewBox="0 0 40 40" fill="none" stroke="#fff" stroke-width="2">
            <path d="M6 34h28M10 34V14l10-7 10 7v20"/>
            <rect x="16" y="22" width="8" height="12"/>
            <path d="M14 17h3M23 17h3"/>
          </svg>
        </div>
        <div class="service-name">Architecture</div>
        <p class="service-text">Thoughtful alterations and renovations planned around the way you live and work.</p>
      </div>
      <div class="service">
        <div class="service-icon">
          <svg width="40" height="40" viewBox="0 0 40 40" fill="none" stroke="#fff" stroke-width="2">
            <circle cx="20" cy="20" r="5"/>
            <circle cx="8" cy="10" r="3"/><circle cx="32" cy="10" r="3"/>
            <circle cx="8" cy="30" r="3"/><circle cx="32" cy="30" r="3"/>
            <path d="M10.5 12l5.5 5M29.5 12l-5.5 5M10.5 28l5.5-5M29.5 28l-5.5-5"/>
          </svg>
        </div>
        <div class="service-name">Project Management</div>
        <p class="service-text">We coordinate every trade on site so your project runs smoothly from start to finish.</p>
      </div>
      <div class="service">
        <div class="service-icon">
          <svg width="40" height="40" viewBox="0 0 40 40" fill="none" stroke="#fff" stroke-width="2.2">
            <circle cx="17" cy="17" r="9"/>
            <path d="M24 24l9 9"/>
          </svg>
        </div>
        <div class="service-name">Research</div>
        <p class="service-text">Careful site checks and material choices that keep quality high and costs clear.</p>
      </div>
    </div>
  </section>

  <section class="project-band">
    <h2 class="section-title">Latest Project</h2>
    <p class="project-text">Our latest commercial fit out brought a tired city office back to life with new partitions, a modern kitchen and a complete services upgrade, finished on time and on budget.</p>
    <span class="button">Read More</span>
  </section>

  <section class="team">
    <h2 class="section-title">Meet Our Team</h2>
    <div class="team-row">
      <span class="arrow-btn">
        <svg width="10" height="10" viewBox="0 0 10 10"><path d="M6.5 1.5L3 5l3.5 3.5" fill="none" stroke="#23417f" stroke-width="1.6"/></svg>
      </span>
      <div class="member">
        <div class="member-photo" role="img" aria-label="Portrait of a team member in a suit"></div>
        <div class="member-name">Liam Carter</div>
        <div class="member-role">Project Manager</div>
      </div>
      <div class="member">
        <div class="member-photo" role="img" aria-label="Portrait of a team member in a suit"></div>
        <div class="member-name">Owen Hale</div>
        <div class="member-role">Site Supervisor</div>
      </div>
      <div class="member">
        <div class="member-photo" role="img" aria-label="Portrait of a team member in a suit"></div>
        <div class="member-name">Ryan Moss</div>
        <div class="member-role">Lead Builder</div>
      </div>
      <div class="member">
        <div class="member-photo" role="img" aria-label="Portrait of a team member in a suit"></div>
        <div class="member-name">Adam Price</div>
        <div class="member-role">Estimator</div>
      </div>
      <span class="arrow-btn">
        <svg width="10" height="10" viewBox="0 0 10 10"><path d="M3.5 1.5L7 5 3.5 8.5" fill="none" stroke="#23417f" stroke-width="1.6"/></svg>
      </span>
    </div>
  </section>

  <footer class="site-footer">
    <div class="footer-cols">
      <div class="footer-col">
        <h4>Navigation</h4>
        <ul><li>Home</li><li>About</li><li>Services</li><li>Projects</li><li>Contact</li></ul>
      </div>
      <div class="footer-col">
        <h4>Our Location</h4>
        <p class="contact-line">
          <svg width="9" height="11" viewBox="0 0 9 11"><path d="M4.5 10.5S1 6.5 1 4.3a3.5 3.5 0 017 0C8 6.5 4.5 10.5 4.5 10.5z" fill="#c4cddd"/></svg>
          14 Kerrigan Street, Dunmore
        </p>
        <p class="contact-line">
          <svg width="10" height="10" viewBox="0 0 10 10"><path d="M2 1l2 2-1 1.5a6 6 0 002.5 2.5L7 6l2 2-1.5 1.5C4.5 9 1 5.5.5 2.5z" fill="#c4cddd"/></svg>
          (09) 555 0142
        </p>
        <p class="contact-line">
          <svg width="11" height="8" viewBox="0 0 11 8"><rect x=".5" y=".5" width="10" height="7" fill="none" stroke="#c4cddd"/><path d="M.5.5l5 4 5-4" fill="none" stroke="#c4cddd"/></svg>
          hello@harwickbuild.example
        </p>
      </div>
      <div class="footer-col">
        <h4>Follow Us</h4>
        <div class="social"><span></span><span></span><span></span><span></span></div>
      </div>
      <div class="footer-col">
        <h4>Subscribe Newsletter</h4>
        <div class="subscribe">
          <span class="subscribe-field">Enter your email</span>
          <span class="subscribe-btn">Sign Up</span>
        </div>
        <div class="footer-brand">Harwick Construction LTD</div>
      </div>
    </div>
    <p class="copyright">© 2024 Harwick Construction LTD. All rights reserved.</p>
  </footer>

</div>
</body>
</html>
```